Construction company Needs a Presentation Folder Design

Construction/Restoration company based in Chicago needs a Presentation Folder for our customers. Folder must have 2 inside pockets with one having a cut for the business card. We focus on residential projects helping our customers to replace roofs, siding, gutters and more... . 80% of our business is HAIL & WIND RESTORATION helping homeowners to navigate through home restoration process when insurance companies gets involved after storms. Final design should communicate professionalism and trust. Our moto is "Trust The Professionals"
Target Market(s)
Chicago local market
Industry/Entity Type
Residential Construction
Font styles to use
Other font styles liked:
- Avenir
Requirements
Must have
- Please incorporate a picture of the storm, since we are Wind and hail restoration contractor
- Services:
- Wind/Hail restoration;
- Roofing;
- Siding;
- Gutters;

Nice to have
- Clean design, Front and Back
- Icons (where applicable)

Should not have
- Should not follow our logo roof line design.
- Don't make a design to simple either, please

```html
<!DOCTYPE html>
<html lang="en">
<head>
<meta charset="utf-8">
<title>Nordic Exteriors Inc. – Presentation Folder</title>
<link href="https://fonts.googleapis.com/css2?family=Montserrat:ital,wght@0,400;0,600;0,700;1,400;1,700&display=swap" rel="stylesheet">
<style>
  :root {
    --page: #ffffff;
    --charcoal: #2f2f31;
    --brand-red: #e3141b;
    --white: #ffffff;
    --dieline: #e0388f;
    --storm-top: #2e3a55;
    --storm-bottom: #6b5a4a;
    --rust-light: #d9836c;
    --rust-dark: #a8402c;
    --tree-light: #b8bdb2;
    --tree-dark: #5d6b4a;
    --sky-top: #2d4668;
    --sky-bottom: #c9ced6;
  }
  html, body {
    margin: 0;
    width: 797px;
    height: 1200px;
    overflow: hidden;
    background: var(--page);
  }
  .canvas {
    position: relative;
    width: 797px;
    height: 1200px;
  }
  .folder-flat {
    position: absolute;
    left: 51px;
    top: 291px;
    width: 694px;
    height: 618px;
    overflow: visible;
    font-family: "Montserrat", Arial, sans-serif;
  }
  .panel { fill: var(--charcoal); }
  .dieline { fill: none; stroke: var(--dieline); stroke-width: 0.8; }
  .fold { stroke: var(--dieline); stroke-width: 0.6; stroke-dasharray: 2 2; }
  .accent-square { fill: var(--brand-red); }
  .card-slit { stroke: var(--brand-red); stroke-width: 0.8; }
  .motto-lead { fill: var(--brand-red); font-size: 15px; font-style: italic; font-weight: 400; }
  .motto-main { fill: var(--white); font-size: 16px; font-weight: 700; }
  .services-title { font-size: 12.5px; font-weight: 700; fill: var(--white); }
  .services-title .hl { fill: var(--brand-red); }
  .services-bar { fill: var(--brand-red); }
  .service-label { fill: var(--white); font-size: 9px; }
  .service-icon { fill: none; stroke: var(--brand-red); stroke-width: 1.6; }
  .service-icon-solid { fill: var(--brand-red); }
  .services-more { fill: var(--white); font-size: 13px; font-style: italic; }
  .services-more b { font-weight: 700; }
  .brand-name { fill: var(--white); font-weight: 600; }
</style>
</head>
<body>
<div class="canvas">
  <svg class="folder-flat" viewBox="0 0 694 618" xmlns="http://www.w3.org/2000/svg">
    <defs>
      <linearGradient id="storm" x1="0" y1="0" x2="0" y2="1">
        <stop offset="0" stop-color="var(--storm-top)"/>
        <stop offset="1" stop-color="var(--storm-bottom)"/>
      </linearGradient>
      <linearGradient id="rust" x1="0" y1="0" x2="1" y2="1">
        <stop offset="0" stop-color="var(--rust-light)"/>
        <stop offset="1" stop-color="var(--rust-dark)"/>
      </linearGradient>
      <linearGradient id="tree" x1="0" y1="0" x2="0" y2="1">
        <stop offset="0" stop-color="var(--tree-light)"/>
        <stop offset="1" stop-color="var(--tree-dark)"/>
      </linearGradient>
      <linearGradient id="sky" x1="0" y1="0" x2="0" y2="1">
        <stop offset="0" stop-color="var(--sky-top)"/>
        <stop offset="1" stop-color="var(--sky-bottom)"/>
      </linearGradient>
    </defs>

    <!-- cover panels -->
    <rect class="panel" x="0" y="0" width="694" height="464"/>
    <!-- pockets -->
    <path class="panel" d="M0 464 H347 L328 618 H0 Z"/>
    <path class="panel" d="M350 464 H694 V618 H366 Z"/>

    <!-- back panel imagery -->
    <rect x="0" y="120" width="115" height="116" fill="url(#storm)" role="img" aria-label="Lightning storm over a house at night"/>
    <rect x="115" y="236" width="232" height="116" fill="url(#rust)" role="img" aria-label="House with a fallen tree after a storm, red duotone"/>

    <!-- front panel imagery -->
    <rect x="347" y="236" width="112" height="116" fill="url(#rust)" role="img" aria-label="Storm-damaged tiled roof, red duotone"/>
    <rect x="347" y="0" width="112" height="120" fill="url(#tree)" role="img" aria-label="Tree fallen across a house yard"/>
    <rect class="accent-square" x="459" y="120" width="115" height="116"/>
    <rect x="574" y="0" width="120" height="120" fill="url(#rust)" role="img" aria-label="Uprooted tree beside a home, red duotone"/>
    <rect x="574" y="236" width="120" height="116" fill="url(#sky)" role="img" aria-label="Dark storm clouds above a house"/>

    <!-- motto -->
    <text class="motto-lead" x="148" y="172">TRUST THE</text>
    <text class="motto-main" x="148" y="193">PROFESSIONALS</text>

    <!-- services -->
    <rect class="services-bar" x="11" y="290" width="2" height="17"/>
    <text class="services-title" x="18" y="303">Our <tspan class="hl">Services</tspan></text>

    <path class="service-icon" d="M23 343 V333 L31 327 L39 333 V343 Z"/>
    <text class="service-label" x="49" y="341">Roofing</text>

    <path class="service-icon-solid" d="M21 371 V361 L28 356 H38 L43 361 V371 Z"/>
    <text class="service-label" x="49" y="369">Siding</text>

    <path class="service-icon" d="M25 403 V391 H37"/>
    <text class="service-label" x="49" y="399">Gutters</text>

    <text class="services-more" x="20" y="422">And <tspan font-weight="700">More.....</tspan></text>

    <!-- company name -->
    <text class="brand-name" x="518" y="417" font-size="30" text-anchor="middle">NORDIC</text>
    <text class="brand-name" x="518" y="438" font-size="14" text-anchor="middle" letter-spacing="1.5">EXTERIORS INC.</text>

    <!-- business card slits -->
    <line class="card-slit" x1="444" y1="524" x2="468" y2="502"/>
    <line class="card-slit" x1="571" y1="585" x2="594" y2="562"/>

    <!-- dieline -->
    <line class="fold" x1="347" y1="0" x2="347" y2="464"/>
    <line class="fold" x1="0" y1="464" x2="694" y2="464"/>
    <path class="dieline" d="M0 0 H694 V618 H366 L350 464 H347 L328 618 H0 Z"/>
  </svg>
</div>
</body>
</html>
```